Job advertisement design

We need an ad design template.
Format: 1/2 page landscape, bleed format: 210 x 136 mm, type area format: 177 x 120 mm
Please design and font accordingly “Flyer back and front”.
Text blocks (examples) see Word doc (can be shortened within the areas if there is too much text).
A template with writable text fields is required so that we can adapt the display independently in the future.

```html
<!DOCTYPE html>
<html lang="de">
<head>
<meta charset="utf-8">
<title>Stellenanzeige Geschäftsführung</title>
<link href="https://fonts.googleapis.com/css2?family=Raleway:wght@400;500;600;700;800&display=swap" rel="stylesheet">
<style>
:root{
  --teal:#4fc3ae;
  --blue:#1b96d3;
  --navy:#1d3a5a;
  --text:#2f3a45;
  --page:#e3e3e3;
  --white:#ffffff;
  --band:linear-gradient(90deg,#55c5b0 0%,#3fb3c0 45%,#1b96d3 100%);
}
*{margin:0;padding:0;box-sizing:border-box}
html,body{width:1200px;height:848px;overflow:hidden;background:var(--page)}
body{font-family:'Raleway',sans-serif;color:var(--text)}
.ad{position:absolute;left:176px;top:149px;width:849px;height:549px;background:var(--white);overflow:hidden}
.band-top{position:absolute;left:283px;top:0;width:566px;height:48px;background:var(--band)}
.band-bottom{position:absolute;left:0;top:518px;width:849px;height:31px;background:var(--band)}
.brand{position:absolute;left:67px;top:68px;display:flex;align-items:center;gap:9px}
.brand-mark{width:16px;height:16px;border-radius:50%;background:var(--teal)}
.brand-name{font-size:21px;font-weight:700;color:var(--navy);line-height:1}
.intro{position:absolute;left:67px;top:137px;width:176px;font-size:11.4px;line-height:15px}
.intro p+p{margin-top:4px}
.intro strong{font-weight:700;color:var(--navy)}
.section{position:absolute;width:234px}
.section h2{display:flex;align-items:center;gap:6px;font-size:13px;font-weight:700;color:var(--teal);margin-bottom:5px;white-space:nowrap}
.section h2 .lead{color:var(--blue)}
.section h2::after{content:"";flex:1;height:1px;background:var(--teal);margin-top:4px}
.ticks{list-style:none;font-size:11.4px;line-height:15px}
.ticks li{position:relative;padding-left:14px;margin-bottom:4px}
.ticks svg{position:absolute;left:0;top:3px;width:9px;height:9px}
.s-offer{left:283px;top:78px}
.s-profile{left:550px;top:78px;width:232px}
.s-tasks{left:283px;top:331px}
.contact-head{position:absolute;left:550px;top:332px;width:232px;text-align:center;font-size:11.4px;line-height:15px;font-weight:700;color:var(--navy)}
.rule{position:absolute;left:550px;width:232px;height:1px;background:var(--navy)}
.rule.r1{top:386px}.rule.r2{top:479px}
.portrait-ring{position:absolute;left:545px;top:395px;width:72px;height:72px}
.portrait{position:absolute;left:553px;top:399px;width:64px;height:64px;border-radius:50%;background:radial-gradient(circle at 50% 45%,#6e6e6e,#1a1a1a 70%)}
.person{position:absolute;left:628px;top:392px}
.person-name{font-size:12px;font-weight:700;color:var(--teal)}
.person-firm{font-size:9px;line-height:11px;color:var(--teal);margin-top:3px;font-weight:500}
.person-line{display:flex;align-items:center;gap:5px;font-size:11.4px;font-weight:700;color:var(--blue)}
.person-line svg{width:9px;height:9px}
.l-phone{margin-top:8px}.l-mail{margin-top:6px}
.web{position:absolute;left:550px;top:484px;width:232px;text-align:center;font-size:9px;font-weight:700;color:var(--navy)}
</style>
</head>
<body>
<div class="ad">
  <div class="band-top"></div>

  <div class="brand"><span class="brand-mark"></span><span class="brand-name">Velmont Beratung</span></div>

  <div class="intro">
    <p>Im Auftrag unseres Kunden suchen wir im Rahmen einer strukturierten Altersnachfolge die Geschäftsführung (w/m/d) für <strong>das Kreisklinikum St. Elisabeth-Hospital in Nordhafen.</strong></p>
    <p>Der Träger Die Caritana Nord gGmbH ist eine regionale Betriebsgesellschaft der Caritana Deutschland gGmbH mit dem Ziel, die ganzheitliche Lösung für alle medizinischen Anliegen in dieser Region aus einer Hand darzustellen: von der Gesundheitsvorsorge, der stationären sowie ambulanten Behandlung im Krankenhaus über die Rehabilitation, bis hin zur Versorgung und Pflege zu Hause oder in Altenpflegeeinrichtungen.</p>
  </div>

  <section class="section s-offer">
    <h2><span><span class="lead">Was</span> Sie erwartet</span></h2>
    <ul class="ticks">
      <li><svg viewBox="0 0 10 10"><rect x=".5" y="1.5" width="8" height="8" fill="none" stroke="#4fc3ae"/><path d="M2.5 5l2 2 5-6" fill="none" stroke="#4fc3ae" stroke-width="1.2"/></svg>Möglichkeit, ein erfolgreiches, traditionsreiches Krankenhaus durch die gesundheitspolitischen Herausforderungen der kommenden Jahre zu führen</li>
      <li><svg viewBox="0 0 10 10"><rect x=".5" y="1.5" width="8" height="8" fill="none" stroke="#4fc3ae"/><path d="M2.5 5l2 2 5-6" fill="none" stroke="#4fc3ae" stroke-width="1.2"/></svg>Die Chance, Ihre Ideen und Konzepte einer zukunftsweisenden Gesundheitsversorgung in dem Fusionsprojekt einzubringen</li>
      <li><svg viewBox="0 0 10 10"><rect x=".5" y="1.5" width="8" height="8" fill="none" stroke="#4fc3ae"/><path d="M2.5 5l2 2 5-6" fill="none" stroke="#4fc3ae" stroke-width="1.2"/></svg>Flache Hierarchien sowie eine moderne und unbürokratische Arbeitsatmosphäre</li>
      <li><svg viewBox="0 0 10 10"><rect x=".5" y="1.5" width="8" height="8" fill="none" stroke="#4fc3ae"/><path d="M2.5 5l2 2 5-6" fill="none" stroke="#4fc3ae" stroke-width="1.2"/></svg>Ein attraktives finanzielles Vergütungspaket</li>
    </ul>
  </section>

  <section class="section s-profile">
    <h2><span><span class="lead">Was</span> Sie mitbringen</span></h2>
    <ul class="ticks">
      <li><svg viewBox="0 0 10 10"><rect x=".5" y="1.5" width="8" height="8" fill="none" stroke="#4fc3ae"/><path d="M2.5 5l2 2 5-6" fill="none" stroke="#4fc3ae" stroke-width="1.2"/></svg>Abgeschlossenes betriebswirtschaftliches Studium mit Schwerpunkt Gesundheitsökonomie bzw. Krankenhausbetriebswirtschaft oder eine vergleichbare Qualifikation</li>
      <li><svg viewBox="0 0 10 10"><rect x=".5" y="1.5" width="8" height="8" fill="none" stroke="#4fc3ae"/><path d="M2.5 5l2 2 5-6" fill="none" stroke="#4fc3ae" stroke-width="1.2"/></svg>Mehrjährige Leitungserfahrung in der Gesundheitswirtschaft, idealerweise im Krankenhausmanagement</li>
      <li><svg viewBox="0 0 10 10"><rect x=".5" y="1.5" width="8" height="8" fill="none" stroke="#4fc3ae"/><path d="M2.5 5l2 2 5-6" fill="none" stroke="#4fc3ae" stroke-width="1.2"/></svg>Ausgeprägte Planungs- und Steuerungskompetenz</li>
      <li><svg viewBox="0 0 10 10"><rect x=".5" y="1.5" width="8" height="8" fill="none" stroke="#4fc3ae"/><path d="M2.5 5l2 2 5-6" fill="none" stroke="#4fc3ae" stroke-width="1.2"/></svg>Kommunikationsstarke und charismatische Persönlichkeit</li>
    </ul>
  </section>

  <section class="section s-tasks">
    <h2><span><span class="lead">Was</span> Sie umsetzen</span></h2>
    <ul class="ticks">
      <li><svg viewBox="0 0 10 10"><rect x=".5" y="1.5" width="8" height="8" fill="none" stroke="#4fc3ae"/><path d="M2.5 5l2 2 5-6" fill="none" stroke="#4fc3ae" stroke-width="1.2"/></svg>Strategisches und operatives Führen des Krankenhauses</li>
      <li><svg viewBox="0 0 10 10"><rect x=".5" y="1.5" width="8" height="8" fill="none" stroke="#4fc3ae"/><path d="M2.5 5l2 2 5-6" fill="none" stroke="#4fc3ae" stroke-width="1.2"/></svg>Erfolgreiches Umsetzen von<br>Digitalisierungsprojekten und<br>Change-Management</li>
      <li><svg viewBox="0 0 10 10"><rect x=".5" y="1.5" width="8" height="8" fill="none" stroke="#4fc3ae"/><path d="M2.5 5l2 2 5-6" fill="none" stroke="#4fc3ae" stroke-width="1.2"/></svg>Erstellung, Abstimmung und Umsetzung eines zukunftsfähigen Konzepts für Medizin, Pflege &amp; Verwaltung mit dem Fusionspartner</li>
    </ul>
  </section>

  <div class="contact-head">Für weitere Informationen sprechen<br>Sie uns gerne direkt an –<br>wir freuen uns auf Sie:</div>
  <div class="rule r1"></div>

  <svg class="portrait-ring" viewBox="0 0 72 72" aria-hidden="true">
    <path d="M30 4 A32 32 0 1 0 64 44" fill="none" stroke="#1b96d3" stroke-width="5"/>
    <path d="M40 2 A34 34 0 0 1 70 30" fill="none" stroke="#4fc3ae" stroke-width="4"/>
  </svg>
  <div class="portrait" role="img" aria-label="Porträtfoto der Ansprechperson"></div>

  <div class="person">
    <div class="person-name">Jonas Berkholz</div>
    <div class="person-firm">VELMONT BERATUNG IM<br>GESUNDHEITSWESEN</div>
    <div class="person-line l-phone"><svg viewBox="0 0 10 10"><path d="M2 1l2 2-1 1.5c.6 1.2 1.3 1.9 2.5 2.5L7 6l2 2-1.5 1.5C4.5 9 1 5.5.5 2.5z" fill="none" stroke="#1b96d3" stroke-width=".8"/></svg>+49 170 000 12 34</div>
    <div class="person-line l-mail"><svg viewBox="0 0 10 10"><rect x=".5" y="2" width="9" height="6.5" fill="none" stroke="#1b96d3" stroke-width=".8"/><path d="M.5 2l4.5 3.5L9.5 2" fill="none" stroke="#1b96d3" stroke-width=".8"/></svg>jb@velmont-beratung.de</div>
  </div>

  <div class="rule r2"></div>
  <div class="web">www.velmont-beratung.de</div>

  <div class="band-bottom"></div>
</div>
</body>
</html>
```